Kitchen and cabinets Landing Page design

Hi there
Web Design Task Outline
• Create a Web Design
• Uncoded webpage layout design
• Single Page - Just Homepage Layout
Task Description
* While we need to update our website, we are actually looking at working with a web designer long-term, which will include quite regular design work. So even though this is a small job, we’d love you to respond, as if you do a good job on this one, we would love to continue working with you on a more regular basis.
Please find below all the information for the design of our new website.
The current Web site is www.marrowbank.com.au – don’t laugh!!!
Site Basics:
The site will be the landing page and online home of our kitchen renovation business. We also do vanities, bedroom robes and general cabinetery for the house and office.
Target audience:
? Predominantly home renovation seekers, families (females – decision maker) and builders.
? Most of our business comes from referrals and recommendations, but the site needs to be updated to improve our on line image
General feeling to be conveyed:
Update our old, tired 80’s site (fresh, modern and vital)
Must portray contemporary and up to date attitude - eye-catching / attention grabbing
But not too expensive looking as to alienate people who may think we look too expensive
Landing Page:
Happy to look at your creativity, but must contain a capturing image, contact details (phone), testimonials
Potential Nav Links =
Home
Photo Gallery
Contact Us
Testimonial
Vanities
Entertainment Units
Colours:
Our business has little to do with wood now so the timber look is superseded. We are open to your creative suggestions. We need all marketing media to be consistent and the website can start this process. Our logo is really weak and dated as well. At present we have a green and blue business card with capital QP logo (hmmm), but we’re generally thinking something that represents the home and kitchen
Layout: Open to your creativity
* Samples of Other Good (Similar) Sites We Like:
www.hobplexa.com.au
www.vorny.com.au
www.primacabinetry.com.au/
www.lunafitouts.com.au
www.thejoinerycourt.com.au
Header Text =
Feel free to submit something from your own creative ideas.
Header Image/photo Ideas:
As the site is about kitchen and house hold cabinets, feel free to use an image to reflect that. We are generally thinking to have one main image that is quite eye-catching and attention grabbing. We can supply photos from jobs we have done later.
* Notes:
1. Do not feel completely bound to these ideas. Feel free to convey the basic idea however your creativity desires.
Thanks a lot and look forward to receiving your first design!
Cheers
Gordon
Updates
sorry people - forgot to mention our best selling point!
we were established in 1980, so have been going for 30 years. This is a strong selling point.
We use "30 years of excellence" as a tag.
there are numerous ways of using est. 1980, ie gold label, starburst etc. Go for it.
thanks
Gordon
Hi Designers, My apologies for the delay in responding to your designs. I have been working on other business and have not had a chance to look at them thoroughly. I plan to focus on them today and will provide feedback. Thank you for your understanding.
Reason: Today was the first chance I've had to look at designs. Will be actively providing feedback over next fews day. Am looking to make some changes to the a few of the designs received. Thanks everyone for you patience.

```html
<!DOCTYPE html>
<html lang="en">
<head>
<meta charset="utf-8">
<title>Marrow Bank Cabinets &amp; Furniture</title>
<link rel="stylesheet" href="https://fonts.googleapis.com/css2?family=Cormorant+Garamond:ital,wght@1,500&family=Tinos&family=Arimo:wght@400;700&display=swap">
<style>
  :root {
    --timber-dark: #d7893a;
    --timber-light: #e6a457;
    --timber-edge: #b86c22;
    --cream: #fdf6e8;
    --ink: #444444;
    --ink-soft: #555555;
    --accent: #d4883a;
    --page-top: #dcdcdc;
    --page-bottom: #ffffff;
    --panel: #f7f5f4;
    --panel-border: #d6d3d1;
    --rule: #8a8a8a;
  }
  * { margin: 0; padding: 0; box-sizing: border-box; }
  html, body { width: 1200px; height: 1100px; overflow: hidden; }
  body {
    position: relative;
    background: linear-gradient(180deg, var(--page-top) 160px, #f2f2f2 700px, var(--page-bottom) 1040px);
    font-family: "Arimo", Arial, sans-serif;
    color: var(--ink);
  }
  .site-header {
    position: absolute; left: 0; top: 0; width: 1200px; height: 164px;
    background: linear-gradient(180deg, var(--timber-light), var(--timber-dark));
    border-bottom: 3px solid var(--timber-edge);
    box-shadow: 0 3px 6px rgba(0,0,0,0.25);
  }
  .brand {
    position: absolute; left: 44px; top: 22px; display: flex; align-items: center; gap: 14px;
  }
  .brand-dot { width: 26px; height: 26px; border-radius: 50%; background: var(--cream); }
  .brand-name {
    font-family: "Cormorant Garamond", Georgia, serif; font-style: italic; font-weight: 500;
    font-size: 40px; color: var(--cream);
  }
  .header-tag {
    position: absolute; right: 38px; top: 38px; text-align: left;
    font-family: "Cormorant Garamond", Georgia, serif; font-style: italic; font-weight: 500;
    font-size: 39px; line-height: 44px; color: var(--cream); letter-spacing: 0.5px;
  }
  .services {
    position: absolute; left: 0; top: 188px; width: 1200px; text-align: center;
    font-family: "Cormorant Garamond", Georgia, serif; font-style: italic; font-weight: 500;
    font-size: 20px; color: var(--ink-soft);
  }
  .photo {
    position: absolute; background: #fff; padding: 8px;
    border-radius: 5px; box-shadow: 0 1px 6px rgba(0,0,0,0.3);
  }
  .photo-fill { width: 100%; height: 100%; }
  .photo-bathroom { left: 78px; top: 258px; width: 262px; height: 313px; }
  .photo-bathroom .photo-fill { background: linear-gradient(135deg, #ece4da, #c9b39a 70%, #a9876a); }
  .photo-lounge { left: 860px; top: 258px; width: 259px; height: 313px; }
  .photo-lounge .photo-fill { background: linear-gradient(160deg, #b9a386, #8d7558 60%, #5d4a36); }
  .photo-kitchen { left: 328px; top: 232px; width: 545px; height: 363px; z-index: 2; }
  .photo-kitchen .photo-fill { background: linear-gradient(180deg, #e9e6e1 0%, #d6d1ca 55%, #6a4130 85%, #4a2a1c); }
  .caption {
    position: absolute; left: 0; top: 616px; width: 1200px; text-align: center;
    font-family: "Cormorant Garamond", Georgia, serif; font-style: italic; font-weight: 500;
    font-size: 21px; color: var(--ink-soft);
  }
  .tagline {
    position: absolute; left: 39px; top: 657px; width: 1124px; height: 72px;
    border-top: 1px solid var(--rule); border-bottom: 1px solid var(--rule);
    text-align: center; line-height: 70px;
    font-family: "Cormorant Garamond", Georgia, serif; font-style: italic; font-weight: 500;
    font-size: 45px; color: var(--ink);
  }
  .column { position: absolute; top: 764px; width: 368px; }
  .col-mission { left: 39px; }
  .col-testimonial { left: 417px; }
  .col-quote { left: 795px; }
  .column h2 {
    font-family: "Tinos", Georgia, serif; font-weight: 400; font-size: 26px;
    color: var(--accent); margin-bottom: 12px; letter-spacing: 0.3px;
  }
  .panel {
    background: var(--panel); border: 1px solid var(--panel-border);
    font-size: 14px; line-height: 21px; color: #333;
  }
  .mission-lead { padding: 8px 11px; height: 36px; margin-bottom: 12px; }
  .mission-body { padding: 10px 11px; height: 165px; }
  .testimonial-box { padding: 10px 13px; height: 216px; }
  .testimonial-box cite { font-style: normal; font-weight: 700; display: block; }
  .quote-box { padding: 8px 8px; height: 216px; line-height: 28px; font-size: 13.5px; }
  .quote-box strong { font-weight: 700; }
  .quote-box a { color: var(--accent); font-weight: 700; }
  .site-footer {
    position: absolute; left: 0; top: 1043px; width: 1200px; height: 57px;
    background: linear-gradient(180deg, var(--timber-light), var(--timber-dark));
    border-top: 2px solid var(--timber-edge);
    text-align: center; line-height: 55px; font-size: 12.5px; color: var(--cream);
  }
</style>
</head>
<body>
  <header class="site-header">
    <div class="brand">
      <span class="brand-dot"></span>
      <span class="brand-name">Marrow Bank</span>
    </div>
    <div class="header-tag">EST. 1980<br>30 YEARS OF EXCELLENCE</div>
  </header>

  <p class="services">We custom design, build and install quality cabinets, kitchens, bathrooms, laundries, home theatres, entertainment units, studies and wardrobes.</p>

  <div class="photo photo-bathroom"><div class="photo-fill" role="img" aria-label="Photo of a white bathroom vanity with flowers"></div></div>
  <div class="photo photo-lounge"><div class="photo-fill" role="img" aria-label="Photo of a timber entertainment unit with television and fireplace"></div></div>
  <div class="photo photo-kitchen"><div class="photo-fill" role="img" aria-label="Photo of a white kitchen with island bench and timber floor"></div></div>

  <p class="caption">Marrow Bank bathroom vanity as featured in HOME NEST Magazine, June 2011</p>

  <div class="tagline">Creating Style and Comfort with Cutting-Edge Technology...</div>

  <section class="column col-mission">
    <h2>OUR MISSION</h2>
    <div class="panel mission-lead">To produce excellent quality cabinetry every time!</div>
    <div class="panel mission-body">We cater for those who truly care about quality, workmanship and a high level of personal service. We are proud of our innovative designs, superior products and outstanding service sought after by the discerning customer.</div>
  </section>

  <section class="column col-testimonial">
    <h2>TESTIMONIAL</h2>
    <blockquote class="panel testimonial-box">"The advice we received from everyone at Marrow Bank was sound, considered and sensitive. We appreciated the staff being here at the time and date arranged and all were a pleasure to deal with. As well as being extremely competent, we felt they took a distinctly personal interest in the kitchen design and construction, always sensitive to our needs and situation."
      <cite>Owen and Tessa Harlow, Brindle Park</cite>
    </blockquote>
  </section>

  <section class="column col-quote">
    <h2>FREE QUOTE</h2>
    <div class="panel quote-box">
      For a NO OBLIGATION FREE quote and consultation see contact details below:<br>
      <strong>PHONE: 9460 2718</strong><br>
      <strong>FAX: 9460 2790</strong><br>
      <strong>ADDRESS: Factory 3, 418 Calder Parade</strong><br>
      <strong>Elmstone Vale, 3174</strong><br>
      <strong>EMAIL:</strong> <a href="#">gordon@marrowbank.com.au</a>
    </div>
  </section>

  <footer class="site-footer">Marrowbankcabinets&amp;furniture © 2011 . All Rights Reserved</footer>
</body>
</html>
```